Business Card Design Project

I need a business card design for our new logo, please check the logo at the following link:
https://www.filecrate.net/s/q7rtx2pw9kd41m/FernLoop.png
The address on the business card:
Av. Gervásio Tavares 418 sala 207
Barra da Tijuca, Rio de Janeiro, RJ
CEP: 22714-380
Brasil
Phone: +55 21 86347215
e-mail: osvaldo@fernloop.com.br
Updates
Thank you all for sending your designs, we will not provide feedback because there are too many designs, on December 3 we will pick the best design according to our point of view. Please keep posting.
Osvaldo
Industry/Entity Type
Business
Look and feel
Each slider illustrates characteristics of the customer's brand and the style your logo design should communicate.

```html
<!DOCTYPE html>
<html lang="pt-BR">
<head>
<meta charset="utf-8">
<title>FernLoop – Business Card</title>
<link rel="stylesheet" href="https://fonts.googleapis.com/css2?family=Open+Sans:wght@400;600;700&display=swap">
<style>
  :root {
    --backdrop: #d9d9d9;
    --brand-yellow: #f2c418;
    --brand-yellow-light: #fbe36a;
    --ink: #1b1b1b;
    --card-dark: #3a3a3a;
    --card-darker: #1c1c1c;
    --panel-black: #141414;
    --wordmark-light: #e6e6e6;
  }
  html, body {
    margin: 0;
    padding: 0;
    width: 1200px;
    height: 1200px;
    overflow: hidden;
    background: var(--backdrop);
    font-family: "Open Sans", Arial, sans-serif;
  }
  .canvas {
    position: relative;
    width: 1200px;
    height: 1200px;
  }
  .card {
    position: absolute;
    left: 250px;
    width: 700px;
    height: 400px;
    border-radius: 6px;
    overflow: hidden;
    box-shadow: 0 6px 18px rgba(0,0,0,0.18);
  }

  /* Front */
  .card-front {
    top: 150px;
    background: radial-gradient(ellipse at 48% 50%, var(--brand-yellow-light) 0%, var(--brand-yellow) 55%, #e8b80f 100%);
    display: flex;
    align-items: center;
    justify-content: center;
    gap: 22px;
  }
  .front-mark {
    width: 46px;
    height: 46px;
    border-radius: 50%;
    background: var(--ink);
  }
  .front-wordmark {
    font-size: 88px;
    font-weight: 700;
    color: var(--ink);
    letter-spacing: -1px;
  }

  /* Back */
  .card-back {
    top: 650px;
    background: linear-gradient(160deg, var(--card-dark) 0%, var(--card-darker) 100%);
  }
  .contact-panel {
    position: absolute;
    top: 0;
    right: 0;
    width: 260px;
    height: 100%;
    background: linear-gradient(180deg, #262626 0%, var(--panel-black) 100%);
    box-shadow: -4px 0 10px rgba(0,0,0,0.35);
    padding: 118px 0 0 26px;
    box-sizing: border-box;
    color: var(--brand-yellow);
    font-size: 15px;
    line-height: 1.35;
  }
  .contact-panel p { margin: 0 0 14px; }
  .name-band {
    position: absolute;
    top: 132px;
    left: 170px;
    width: 270px;
    height: 70px;
    background: var(--brand-yellow);
    box-sizing: border-box;
    padding: 6px 16px 0 0;
    text-align: right;
    color: var(--ink);
  }
  .person-name {
    display: block;
    font-size: 24px;
    font-weight: 400;
  }
  .person-role {
    display: block;
    font-size: 20px;
    font-weight: 400;
  }
  .back-wordmark {
    position: absolute;
    left: 26px;
    bottom: 70px;
    font-size: 84px;
    font-weight: 700;
    color: var(--wordmark-light);
    letter-spacing: -1px;
  }
</style>
</head>
<body>
<main class="canvas">
  <section class="card card-front" aria-label="Business card front">
    <span class="front-mark" aria-hidden="true"></span>
    <span class="front-wordmark">FernLoop</span>
  </section>

  <section class="card card-back" aria-label="Business card back">
    <div class="back-wordmark">FernLoop</div>
    <div class="name-band">
      <span class="person-name">Firstname Lastname</span>
      <span class="person-role">Function</span>
    </div>
    <address class="contact-panel" style="font-style:normal">
      <p>Av. Gervásio Tavares 418 sala 207<br>
         Barra da Tijuca, Rio de Janeiro, RJ<br>
         CEP: 22714-380<br>
         Brasil</p>
      <p>+55 21 86347215</p>
      <p>osvaldo@fernloop.com.br</p>
    </address>
  </section>
</main>
</body>
</html>
```